Launch Website

A very simple, but attractive website (template preferred) is required in a common format - HTML5 or Wordpress etc.
It should be easily user updateable for updates.
Pages it needs:
-Home Page with menu bar, company logo and 1 large graphic/picture and two smaller graphics/logos.
- What we do
- How we do it
- About Us
- Guarantees
- Results
- Contact Page with Enquiry Form
- Provision for a blog to be added later

Most pages will be approx 150 words text with some small/medium images.
We have our own domain & hosting.

A "less is more" design approach would be encouraged.

Target Market(s)

Vehicle Fleet Managers

Industry/Entity Type

It Company

Font styles to use
Sans Serif

Colors
9bcb3c

Requirements
Must have
• Corporate Style. No Fluff.
Nice to have
• Images of LIght Commerical vehicles and trucks

Am ok with white background throughout site.
Colours should match/complement company logo.
Should not have
• Should not be too "busy"

```html
<!DOCTYPE html>
<html lang="en">
<head>
<meta charset="utf-8">
<title>Corvane Transit</title>
<link rel="stylesheet" href="https://fonts.googleapis.com/css2?family=PT+Sans:wght@400;700&family=PT+Sans+Narrow:wght@400;700&family=Arimo:wght@400;700&display=swap">
<style>
:root{
  --green:#009b45;
  --ink:#1e2029;
  --slate:#3d4350;
  --grey:#7a7a7a;
  --title:#555;
  --white:#fff;
}
*{box-sizing:border-box;margin:0;padding:0}
html,body{width:758px;height:1200px;overflow:hidden;background:var(--white)}
body{position:relative;font-family:"PT Sans Narrow",sans-serif}
.abs{position:absolute}

/* header */
.brand{left:19px;top:20px;display:flex;align-items:center;gap:10px}
.brand-mark{width:26px;height:26px;border-radius:50%;background:var(--green)}
.brand-name{font-family:"PT Sans",sans-serif;font-size:34px;font-weight:700;line-height:36px;color:var(--green)}
.badge-partner{left:527px;top:40px;width:113px;height:25px;border-radius:6px;background:var(--ink);border:1px solid #555}
.badge-member{left:658px;top:22px;width:78px;height:40px;border-radius:4px;background:#c9ccd1}

/* nav + hero */
.hero-band{left:0;top:75px;width:758px;height:243px;background:var(--ink)}
.nav{left:14px;top:75px;width:730px;height:33px;display:flex}
.nav a{color:var(--white);text-decoration:none;font-family:"PT Sans",sans-serif;font-size:12px;line-height:33px;text-align:center}
.nav a.active{background:var(--green)}
.hero-frame{left:14px;top:108px;width:730px;height:300px;background:var(--white)}
.hero{left:20px;top:114px;width:717px;height:289px;background:linear-gradient(100deg,#c9a31c 0%,#f4e06a 22%,#d8d6c8 45%,#b9b7c2 65%,#6b7a3a 100%)}

/* features */
.feature{width:314px}
.feature svg{position:absolute;left:0;top:0}
.feature h3{margin-left:64px;font-size:14px;line-height:16px;color:var(--title);font-weight:400}
.feature p{margin-left:64px;font-size:10px;line-height:13px;color:var(--grey);margin-top:3px}

/* testimonials */
.testimonials{left:0;top:609px;width:758px;height:241px;background:linear-gradient(90deg,#3a3a3a,#2c2c2c 40%,#4a4646 75%,#3a3636)}
.testimonials h2{position:absolute;top:26px;width:100%;text-align:center;color:var(--white);font-family:"PT Sans",sans-serif;font-size:27px;font-weight:700}
.avatar{width:36px;height:36px;background:#8a8f99;border:1px solid #ddd}
.quote{width:274px;height:78px;background:var(--white);padding:9px 13px;font-family:Arimo,sans-serif;font-size:9px;line-height:11.2px;color:#222}
.quote::before{content:"";position:absolute;left:-14px;top:14px;border-style:solid;border-width:0 14px 11px 0;border-color:transparent var(--white) transparent transparent}
.author{font-family:Arimo,sans-serif;color:var(--white);font-size:9px}
.author b{display:block;font-size:11px}

/* news */
.post{width:290px}
.date{position:absolute;left:0;top:0;width:42px;height:52px;background:var(--slate);color:var(--white);text-align:center}
.date span{display:block;background:var(--green);font-size:9px;line-height:13px}
.date strong{display:block;font-size:17px;line-height:38px;font-weight:400}
.post h4{margin-left:56px;font-size:11.5px;line-height:13px;color:var(--title)}
.post p{margin-left:56px;font-size:9.5px;line-height:11.5px;color:var(--grey);margin-top:5px}

/* footer */
.footer{left:0;top:1066px;width:758px;height:134px;background:var(--green);color:var(--white);font-family:Arimo,sans-serif;text-align:center}
.social{position:absolute;left:267px;top:26px;display:flex;gap:10px}
.social span{width:34px;height:34px;border-radius:50%;background:var(--white)}
.footer-links{position:absolute;top:80px;width:100%;font-size:9.5px}
.copyright{position:absolute;top:96px;width:100%;font-size:8px}
</style>
</head>
<body>
<header>
  <div class="abs brand">
    <span class="brand-mark" aria-hidden="true"></span>
    <span class="brand-name">Corvane Transit</span>
  </div>
  <div class="abs badge-partner" aria-hidden="true"></div>
  <div class="abs badge-member" aria-hidden="true"></div>
</header>

<div class="abs hero-band"></div>
<nav class="abs nav">
  <a class="active" href="#" style="width:80px">HOME</a>
  <a href="#" style="width:110px">WHAT WE DO</a>
  <a href="#" style="width:118px">HOW WE DO IT</a>
  <a href="#" style="width:100px">ABOUT US</a>
  <a href="#" style="width:112px">GUARANTEES</a>
  <a href="#" style="width:94px">RESULTS</a>
  <a href="#" style="width:116px">CONTACT US</a>
</nav>
<div class="abs hero-frame"></div>
<div class="abs hero" role="img" aria-label="Photo of a white truck driving on a country road at sunrise"></div>

<section>
  <div class="abs feature" style="left:42px;top:435px">
    <svg width="50" height="45" viewBox="0 0 50 45"><g fill="#009b45"><rect x="0" y="12" width="11" height="24"/><rect x="18" y="22" width="11" height="14"/><rect x="36" y="0" width="11" height="36"/><rect x="0" y="40" width="50" height="4"/></g></svg>
    <h3>Progress to Trial</h3>
    <p>Lorem ipsum dolor sit amet, consectetuer adipiscing elit, sed diam nonummy nibh euismod tincidunt ut laoreet dolore magna aliquam erat volutpat. Ut wisi enim ad minim veniam, quis nostrud.</p>
  </div>
  <div class="abs feature" style="left:420px;top:435px">
    <svg width="48" height="48" viewBox="0 0 48 48"><g fill="none" stroke="#009b45" stroke-width="5" stroke-linejoin="round"><path d="M30 6H8a4 4 0 0 0-4 4v30a4 4 0 0 0 4 4h30a4 4 0 0 0 4-4V22"/></g><path d="M38 2l7 7-20 20-9 2 2-9z" fill="#009b45"/></svg>
    <h3>Assess Trial Results</h3>
    <p>Adipiscing elit, sed diam nonummy nibh euismod tincidunt ut laoreet dolore magna aliquam erat volutpat. Ut wisi enim ad minim veniam, quis nostrud exerci tation ullamcorper.</p>
  </div>
  <div class="abs feature" style="left:42px;top:520px">
    <svg width="50" height="36" viewBox="0 0 50 36"><path fill="#009b45" d="M0 2h30v26H0zM32 8h9l9 10v10H32z"/><circle cx="8" cy="31" r="4" fill="#009b45" stroke="#fff" stroke-width="2"/><circle cx="41" cy="31" r="4" fill="#009b45" stroke="#fff" stroke-width="2"/></svg>
    <h3>Rollout to balance of Fleet</h3>
    <p>Diam nonummy nibh euismod tincidunt ut laoreet dolore magna aliquam erat volutpat. Ut wisi enim ad minim veniam, quis nostrud exerci tation ullamcorper suscipit lobortis nisl ut aliquip ex.</p>
  </div>
  <div class="abs feature" style="left:420px;top:520px">
    <svg width="48" height="48" viewBox="0 0 48 48"><rect x="2" y="2" width="44" height="44" fill="#009b45"/><rect x="7" y="13" width="34" height="28" fill="#fff"/><path d="M9 33l7-9 6 8 6-10 5 7 6-5" fill="none" stroke="#009b45" stroke-width="3"/><g fill="#fff"><rect x="7" y="6" width="3" height="3"/><rect x="12" y="6" width="3" height="3"/><rect x="17" y="6" width="3" height="3"/></g></svg>
    <h3>Monitor ongoing cost savings</h3>
    <p>Lorem ipsum dolor sit amet, consectetuer adipiscing elit, sed diam nonummy nibh euismod tincidunt ut laoreet dolore magna aliquam erat volutpat. Ut wisi enim ad minim veniam.</p>
  </div>
</section>

<section class="abs testimonials" role="img" aria-label="Dimmed photo of business people talking">
  <h2>Our Testimonials</h2>
  <div class="abs avatar" style="left:28px;top:100px" role="img" aria-label="Portrait of client"></div>
  <div class="abs quote" style="left:86px;top:86px">"Lorem ipsum dolor sit amet, consectetuer adipiscing elit, sed diam nonummy nibh euismod tincidunt ut laoreet dolore magna aliquam erat volutpat. Ut wisi enim ad minim veniam, quis nostrud exerci tation ullamcorper suscipit lobortis nisl ut aliquip ex ea commodo consequat."</div>
  <div class="abs author" style="left:87px;top:172px"><b>Dale Morrow</b>Founder, Northline Co</div>
  <div class="abs avatar" style="left:391px;top:100px" role="img" aria-label="Portrait of client"></div>
  <div class="abs quote" style="left:449px;top:86px">"Lorem ipsum dolor sit amet, consectetuer adipiscing elit, sed diam nonummy nibh euismod tincidunt ut laoreet dolore magna aliquam erat volutpat. Ut wisi enim ad minim veniam, quis nostrud exerci tation ullamcorper suscipit lobortis nisl ut aliquip ex ea commodo consequat."</div>
  <div class="abs author" style="left:450px;top:172px"><b>T. Hollis</b>Marketer of Senior Products</div>
</section>

<section>
  <div class="abs post" style="left:52px;top:890px">
    <div class="date"><span>JUN</span><strong>18</strong></div>
    <h4>Lorem ipsum dolor sit amet, consectetuer adipiscing elit, sed diam nonummy nibh euismod.</h4>
    <p>Ipsum dolor sit amet, consectetuer adipiscing elit, sed diam nonummy nibh euismod tincidunt ut laoreet dolore.</p>
  </div>
  <div class="abs post" style="left:401px;top:890px">
    <div class="date"><span>JUN</span><strong>18</strong></div>
    <h4>Magna aliquam erat volutpat. Ut wisi enim ad minim veniam, quis nostrud exerci tation ullamcorper</h4>
    <p>Nummy nibh euismod tincidunt ut laoreet dolore magna aliquam erat volutpat. Ut wisi enim ad minim veniam, quis.</p>
  </div>
  <div class="abs post" style="left:52px;top:975px">
    <div class="date"><span>FEB</span><strong>21</strong></div>
    <h4>Consectetuer adipiscing elit, sed diam nonummy nibh euismod tincidunt ut laoreet dolore magna.</h4>
    <p>Euismod tincidunt ut laoreet dolore magna aliquam erat volutpat. Ut wisi enim ad minim veniam, quis nostrud.</p>
  </div>
  <div class="abs post" style="left:401px;top:975px">
    <div class="date"><span>FEB</span><strong>21</strong></div>
    <h4>Tation ullamcorper suscipit lobortis nisl ut aliquip ex ea commodo consequat</h4>
    <p>Exerci tation ullamcorper suscipit lobortis nisl ut aliquip ex ea commodo consequat</p>
  </div>
</section>

<footer class="abs footer">
  <div class="social" aria-label="Social links"><span></span><span></span><span></span><span></span><span></span></div>
  <div class="footer-links">Home · About Us · Products · Features · Options · Replacement Parts · FAQ's · Library · Videos · Contact Us</div>
  <div class="copyright">© Copyright 2002 - 2013 Company Name. All Rights Reserved</div>
</footer>
</body>
</html>
```